Wedding Save the Date Design Image

I updated the brief with an additional image that used more negative white space and is a bit more "watercolor" in nature. We are going to have our wedding in Lake Como, Italy, and we need to send out a simple "save the date" invite with a key image that captures the fun and vibe of Lake Como. We are thinknig about mabye an iconic part of Lake Como as the inspiration image... maybe the classib boats on the lake, or some version of Casa Lunetti where we will have the wedding... but the idea is just to create an image that conveys the "essence" or fun/"Italian" vibe of Lake Como to get people excited. Perhaps a "watercolor" style image or other expressive artwork... Definitely not a photo or direct image... this should be more whimsical and "expressive" in artistic tone.

```html
<!DOCTYPE html>
<html lang="en">
<head>
<meta charset="utf-8">
<title>Save the Date – Lake Como</title>
<link rel="stylesheet" href="https://fonts.googleapis.com/css2?family=Barlow:wght@500&family=Yellowtail&display=swap">
<style>
  :root {
    --page: #ffffff;
    --sky: #a9d3ea;
    --mountain: #6fb3b8;
    --village: #e9c9a0;
    --roof: #e07a3c;
    --lake: #2f8fb5;
    --lake-deep: #1d5f86;
    --title-blue: #4a9fd8;
    --title-glow: rgba(160, 215, 255, 0.9);
    --text-light: #f4f4f4;
  }
  * { margin: 0; padding: 0; box-sizing: border-box; }
  html, body {
    width: 974px;
    height: 1200px;
    overflow: hidden;
    background: var(--page);
  }
  .card {
    position: absolute;
    left: 52px;
    top: 20px;
    width: 870px;
    height: 1160px;
    overflow: hidden;
  }
  .scene-art {
    position: absolute;
    inset: 0;
    background:
      radial-gradient(ellipse 55% 45% at 78% 62%, var(--roof) 0%, rgba(224,122,60,0.55) 35%, rgba(233,201,160,0) 70%),
      radial-gradient(ellipse 60% 30% at 65% 22%, rgba(255,255,255,0.85) 0%, rgba(255,255,255,0) 70%),
      linear-gradient(180deg,
        var(--sky) 0%,
        var(--sky) 18%,
        var(--mountain) 38%,
        var(--village) 52%,
        var(--lake) 68%,
        var(--lake-deep) 100%);
  }
  .headline {
    position: absolute;
    left: 76px;
    top: 58px;
    font-family: "Barlow", sans-serif;
    font-weight: 500;
    font-size: 188px;
    line-height: 160px;
    letter-spacing: -2px;
    color: var(--title-blue);
    text-shadow: 0 0 14px var(--title-glow);
  }
  .date {
    position: absolute;
    left: 84px;
    top: 548px;
    font-family: "Barlow", sans-serif;
    font-weight: 500;
    color: var(--text-light);
  }
  .date-day {
    font-size: 54px;
    line-height: 58px;
  }
  .date-year {
    font-size: 142px;
    line-height: 110px;
    letter-spacing: -3px;
  }
  .venue {
    position: absolute;
    left: 86px;
    top: 850px;
    font-family: "Barlow", sans-serif;
    font-weight: 500;
    font-size: 38px;
    color: var(--text-light);
  }
  .couple {
    position: absolute;
    left: 176px;
    top: 960px;
    font-family: "Yellowtail", cursive;
    font-size: 78px;
    color: var(--text-light);
    white-space: nowrap;
  }
</style>
</head>
<body>
  <main class="card">
    <div class="scene-art" role="img" aria-label="Whimsical painted view of a Lake Como village with a bell tower, orange-roofed houses, green mountains, clouds, sailboats on blue water and orange flowers in the foreground"></div>
    <h1 class="headline">SAVE<br>THE<br>DATE</h1>
    <p class="date">
      <span class="date-day">9 MAY</span><br>
      <span class="date-year">20<br>26</span>
    </p>
    <p class="venue">LAKE COMO, ITALY</p>
    <p class="couple">Giulia &amp; Daniel</p>
  </main>
</body>
</html>
```